concrete contractor looking for a business card and logo design
see attached images for inspiration
incorporate cement truck, trowel or finisher in to the design
would like the background to be concrete colored or light grey

Company Name: Vintor Concrete

Concrete Services
Driveways
Patios & Slab
Walkways
Block Walls
Planters/Mowing Strip
Demo/Haul

Need Vintor Concrete logo vectored and spaced/aligned properly

I like Gothic fonts like

Franklin Gothic Demi
Copperplate Gothic Bold

```html
<!DOCTYPE html>
<html lang="en">
<head>
<meta charset="utf-8">
<title>Vintor Concrete – Business Card</title>
<link href="https://fonts.googleapis.com/css2?family=Lato:wght@400;700;900&family=Oswald:wght@500;600&display=swap" rel="stylesheet">
<style>
  :root {
    --page: #dcdcda;
    --card: #f4f3f0;
    --orange: #f39a1e;
    --accent-red: #e2462a;
    --ink: #2e2e30;
    --ink-soft: #555558;
    --band-dark: #2f3033;
  }
  * { margin: 0; padding: 0; box-sizing: border-box; }
  html, body { width: 1200px; height: 900px; overflow: hidden; }
  body {
    background: var(--page);
    font-family: "Lato", Arial, sans-serif;
    color: var(--ink);
    position: relative;
  }
  .card {
    position: absolute;
    left: 250px;
    width: 700px;
    height: 400px;
    background: var(--card);
    box-shadow: 0 6px 18px rgba(0,0,0,0.18);
    overflow: hidden;
  }
  .card--back { top: 30px; }
  .card--front { top: 470px; }

  /* Back side */
  .brand {
    position: absolute;
    right: 40px;
    top: 34px;
    text-align: right;
  }
  .brand__call {
    font-size: 15px;
    font-weight: 700;
    color: var(--ink);
  }
  .brand__phone {
    font-size: 17px;
    font-weight: 900;
    color: var(--accent-red);
    margin-bottom: 6px;
  }
  .brand__mark {
    display: flex;
    align-items: center;
    justify-content: flex-end;
    gap: 8px;
  }
  .brand__dot {
    width: 14px; height: 14px;
    border-radius: 50%;
    background: var(--orange);
  }
  .brand__name {
    font-size: 22px;
    font-weight: 900;
    color: var(--ink);
  }
  .owner {
    position: absolute;
    left: 225px;
    top: 140px;
    text-align: center;
  }
  .owner__name {
    font-family: "Oswald", "Arial Narrow", sans-serif;
    font-weight: 600;
    font-size: 36px;
    letter-spacing: 0.5px;
    line-height: 1;
  }
  .owner__first { color: var(--orange); }
  .owner__last { color: var(--ink); }
  .owner__title {
    font-size: 14px;
    letter-spacing: 2px;
    color: var(--ink-soft);
    margin-top: 4px;
  }
  .divider {
    position: absolute;
    left: 50px;
    right: 60px;
    top: 210px;
    height: 2px;
    background: var(--orange);
  }
  .contact {
    position: absolute;
    left: 36px;
    top: 250px;
    list-style: none;
  }
  .contact li {
    display: flex;
    align-items: center;
    gap: 12px;
    font-size: 19px;
    font-weight: 700;
    color: var(--ink);
    line-height: 1.45;
  }
  .contact svg { width: 18px; height: 18px; flex: none; }
  .address {
    position: absolute;
    right: 40px;
    top: 262px;
    font-size: 19px;
    font-weight: 700;
    line-height: 1.4;
    color: var(--ink);
  }
  .band {
    position: absolute;
    bottom: 0;
    height: 40px;
  }
  .band--orange-left { left: 0; width: 250px; background: var(--orange); }
  .band--dark-right { right: 0; width: 220px; height: 36px; bottom: 0; background: var(--band-dark); }

  /* Front side */
  .worker-art {
    position: absolute;
    left: 285px;
    top: 30px;
    width: 130px;
    height: 150px;
    background: radial-gradient(circle at 50% 45%, #4a4a4d 0%, #6d6d70 55%, rgba(244,243,240,0) 75%);
  }
  .services-heading {
    position: absolute;
    left: 40px;
    right: 40px;
    top: 195px;
    display: flex;
    align-items: center;
    gap: 12px;
  }
  .services-heading::before,
  .services-heading::after {
    content: "";
    flex: 1;
    height: 2px;
    background: var(--orange);
  }
  .services-heading h2 {
    font-family: "Oswald", "Arial Narrow", sans-serif;
    font-weight: 500;
    font-size: 30px;
    color: var(--orange);
    letter-spacing: 0.5px;
  }
  .services {
    position: absolute;
    left: 60px;
    right: 40px;
    top: 252px;
    list-style: none;
    display: flex;
    flex-wrap: wrap;
    justify-content: center;
    column-gap: 26px;
    row-gap: 4px;
  }
  .services li {
    font-size: 18px;
    font-weight: 700;
    color: var(--ink);
    display: flex;
    align-items: center;
    gap: 7px;
  }
  .services li::before {
    content: "";
    width: 9px; height: 9px;
    border-radius: 50%;
    background: var(--orange);
  }
  .services__break { flex-basis: 100%; height: 0; }
  .services__break::before { display: none; }
  .band--orange-full { left: 0; right: 0; height: 52px; background: var(--orange); }
</style>
</head>
<body>

  <section class="card card--back" aria-label="Business card back">
    <div class="brand">
      <div class="brand__call">Call me now</div>
      <div class="brand__phone">775-555-0192</div>
      <div class="brand__mark">
        <span class="brand__dot"></span>
        <span class="brand__name">Vintor Concrete</span>
      </div>
    </div>

    <div class="owner">
      <div class="owner__name"><span class="owner__first">DANIEL</span> <span class="owner__last">MORROW</span></div>
      <div class="owner__title">OWNER</div>
    </div>

    <div class="divider"></div>

    <ul class="contact">
      <li>
        <svg viewBox="0 0 18 18" aria-hidden="true"><circle cx="9" cy="9" r="9" fill="#f39a1e"/><path d="M6 4.5l2 2-1 1.3c.7 1.4 1.8 2.5 3.2 3.2l1.3-1 2 2-1.2 1.5C8.6 13 5 9.4 4.5 5.7z" fill="#fff"/></svg>
        714-555-0148
      </li>
      <li>
        <svg viewBox="0 0 18 18" aria-hidden="true"><circle cx="9" cy="9" r="9" fill="#f39a1e"/><rect x="4.5" y="6" width="9" height="6.5" fill="#fff"/><path d="M4.5 6l4.5 3.6L13.5 6" stroke="#f39a1e" stroke-width="1" fill="none"/></svg>
        hello@vintorconcrete.com
      </li>
      <li>
        <svg viewBox="0 0 18 18" aria-hidden="true"><circle cx="9" cy="9" r="9" fill="#f39a1e"/><circle cx="9" cy="9" r="4.5" stroke="#fff" stroke-width="1.3" fill="none"/><path d="M4.5 9h9M9 4.5c-2 2.5-2 6.5 0 9M9 4.5c2 2.5 2 6.5 0 9" stroke="#fff" stroke-width="1" fill="none"/></svg>
        www.vintorconcrete.com
      </li>
    </ul>

    <div class="address">Unit 4, 218 Granite Ave<br>Riverton CA 92801</div>

    <div class="band band--orange-left" role="img" aria-label="Orange hazard stripe band"></div>
    <div class="band band--dark-right" role="img" aria-label="Dark hazard stripe band"></div>
  </section>

  <section class="card card--front" aria-label="Business card front">
    <div class="worker-art" role="img" aria-label="Illustration of a concrete worker kneeling and finishing a slab with a trowel"></div>

    <div class="services-heading"><h2>CONCRETE SERVICES</h2></div>

    <ul class="services">
      <li>Driveways</li>
      <li>Patios &amp; Slab</li>
      <li>Walkways</li>
      <li>Block &amp; Bick Walls</li>
      <li class="services__break" aria-hidden="true"></li>
      <li>Planters/Mowing Strip</li>
      <li>Demo/Haul</li>
    </ul>

    <div class="band band--orange-full" role="img" aria-label="Orange hazard stripe band"></div>
  </section>

</body>
</html>
```